TEK Logistics - Banner 2.5' x 8' for 20+ locations

Need a banner designed that will pop. This banner will be displayed at over 20 of our transportation facilities. Goal is for the banner to grab the attention of employees, contractors and clients and help reinforce our mission and core values. Designed needs to include TEK Logo, our core values and mission statement. Red and Black are the main company colors and we need to stay within that theme and color pallet. Attached is a previous version that was too basic and boring. Willing to consider a design that excludes the mission statement.

Gathering more feedback

```html
<!DOCTYPE html>
<html lang="en">
<head>
<meta charset="utf-8">
<title>TEK Logistics – Mission &amp; Core Values Banner</title>
<link rel="stylesheet" href="https://fonts.googleapis.com/css2?family=Poppins:wght@400;500;700;800&display=swap">
<style>
  :root {
    --red: #d8311f;
    --red-dark: #b8261a;
    --ink: #1c1c1c;
    --grey-text: #555555;
    --rule: #d6d6d6;
    --white: #ffffff;
    --stage: #c4c4c4;
    --bar-dark: #262626;
  }
  * { margin: 0; padding: 0; box-sizing: border-box; }
  html, body {
    width: 1200px; height: 1200px; overflow: hidden;
    background: var(--stage);
    font-family: "Poppins", sans-serif;
  }
  .banner {
    position: absolute; left: 58px; top: 431px;
    width: 1084px; height: 338px;
    background: var(--white);
    overflow: hidden;
  }
  .mission { position: absolute; color: var(--grey-text); font-size: 19px; font-weight: 400; letter-spacing: 0.2px; white-space: nowrap; text-transform: uppercase; }
  .mission strong { color: var(--red); font-weight: 700; }
  .mission--line1 { left: 26px; top: 13px; }
  .mission--line2 { left: 112px; top: 39px; }
  .mission-band {
    position: absolute; left: 0; top: 71px; width: 760px; height: 30px;
    background: linear-gradient(90deg, var(--red-dark), var(--red) 30%);
  }
  .mission-band__text {
    position: absolute; left: 58px; top: 0; line-height: 30px;
    color: var(--white); font-size: 21px; font-weight: 700; white-space: nowrap;
  }
  .mission-band__text span { font-weight: 400; font-size: 18px; }

  .values { position: absolute; left: 0; top: 124px; }
  .value { position: absolute; width: 130px; text-align: center; top: 0; }
  .value__icon { position: absolute; left: 43px; top: 2px; width: 46px; height: 46px; }
  .value__label {
    position: absolute; left: 0; top: 54px; width: 130px;
    color: var(--grey-text); font-size: 13.5px; line-height: 16.5px;
  }
  .values__rule { position: absolute; top: 0; width: 1px; height: 103px; background: var(--rule); }

  .photo { position: absolute; left: 0; top: 0; width: 1084px; height: 338px; }

  .contact-bar {
    position: absolute; left: 128px; top: 263px; width: 760px; height: 42px;
    background: linear-gradient(90deg, #111 0%, var(--bar-dark) 70%, rgba(60,60,60,0) 100%);
  }
  .contact { position: absolute; top: 0; line-height: 42px; color: var(--white); white-space: nowrap; }
  .contact--phone { left: 75px; font-size: 22px; font-weight: 700; }
  .contact--web { left: 303px; font-size: 21px; font-weight: 400; }
  .contact--web b { font-weight: 700; }
  .contact__icon { position: absolute; top: 11px; width: 20px; height: 20px; }
  .contact-bar__divider { position: absolute; left: 247px; top: 6px; width: 1px; height: 30px; background: #888; }

  .brand {
    position: absolute; left: 22px; top: 260px; width: 100px; height: 50px;
    display: flex; flex-direction: column; justify-content: center; align-items: center;
    color: var(--red); font-weight: 700; line-height: 1;
  }
  .brand__name { font-size: 26px; }
  .brand__sub { font-size: 10px; letter-spacing: 2.5px; margin-top: 3px; }
</style>
</head>
<body>
<main class="banner">
  <p class="mission mission--line1">Provide the <strong>best customer experience</strong> while creating an</p>
  <p class="mission mission--line2"><strong>environment</strong> of <strong>growth</strong> and <strong>opportunity</strong> for our</p>
  <div class="mission-band">
    <p class="mission-band__text">CUSTOMERS, EMPLOYEES, <span>AND</span> SERVICE PROVIDERS.</p>
  </div>

  <svg class="photo" viewBox="0 0 1084 338" aria-hidden="false">
    <defs>
      <linearGradient id="truckTones" x1="0" y1="0" x2="1" y2="1">
        <stop offset="0" stop-color="#b9c2cc"/>
        <stop offset="0.45" stop-color="#d98a72"/>
        <stop offset="1" stop-color="#2b2b2b"/>
      </linearGradient>
    </defs>
    <circle cx="898" cy="166" r="188" fill="var(--red)"/>
    <circle cx="878" cy="168" r="176" fill="var(--white)"/>
    <circle cx="874" cy="170" r="168" fill="url(#truckTones)" role="img" aria-label="Photo of a white semi truck hauling a red shipping container"/>
    <path d="M778 95 C 850 15, 990 20, 1050 110 C 975 45, 860 45, 778 95 Z" fill="var(--white)"/>
  </svg>

  <div class="values">
    <div class="value" style="left:5px">
      <svg class="value__icon" viewBox="0 0 46 46"><circle cx="23" cy="23" r="20" fill="none" stroke="var(--ink)" stroke-width="2"/><path d="M23 2 A21 21 0 0 1 23 44" fill="none" stroke="var(--red)" stroke-width="2.5" transform="translate(2 0)"/><path d="M15 22h4v10h-4z M19 22l4-7c2 0 2 2 1 4h6c2 0 2 3 0 3 2 0 2 3 0 3 1 0 1 3-1 3h-10" fill="none" stroke="var(--ink)" stroke-width="1.3"/></svg>
      <p class="value__label">Do the right things for the right reasons</p>
    </div>
    <span class="values__rule" style="left:135px"></span>
    <div class="value" style="left:138px">
      <svg class="value__icon" viewBox="0 0 46 46"><circle cx="23" cy="23" r="20" fill="none" stroke="var(--ink)" stroke-width="2"/><path d="M23 2 A21 21 0 0 1 23 44" fill="none" stroke="var(--red)" stroke-width="2.5" transform="translate(2 0)"/><path d="M12 28c4 0 7 2 10 2h8l4-4 M23 27v-10 M23 20c-4 0-5-3-5-5 3 0 5 2 5 5z M23 18c0-3 2-5 5-5 0 3-2 5-5 5z" fill="none" stroke="var(--ink)" stroke-width="1.3"/></svg>
      <p class="value__label">Pursue growth and development</p>
    </div>
    <span class="values__rule" style="left:271px"></span>
    <div class="value" style="left:272px">
      <svg class="value__icon" viewBox="0 0 46 46"><circle cx="23" cy="23" r="20" fill="none" stroke="var(--ink)" stroke-width="2"/><path d="M23 2 A21 21 0 0 1 23 44" fill="none" stroke="var(--red)" stroke-width="2.5" transform="translate(2 0)"/><path d="M23 14c3 3 3 8 0 13-3-5-3-10 0-13z M23 27c-4-1-8-4-9-9 4 0 7 3 9 9z M23 27c4-1 8-4 9-9-4 0-7 3-9 9z M13 29h20" fill="none" stroke="var(--ink)" stroke-width="1.3"/></svg>
      <p class="value__label">Build a positive team atmosphere</p>
    </div>
    <span class="values__rule" style="left:404px"></span>
    <div class="value" style="left:406px">
      <svg class="value__icon" viewBox="0 0 46 46"><circle cx="23" cy="23" r="20" fill="none" stroke="var(--ink)" stroke-width="2"/><path d="M23 2 A21 21 0 0 1 23 44" fill="none" stroke="var(--red)" stroke-width="2.5" transform="translate(2 0)"/><path d="M17 20h12v9H17z M29 23h4l2 3v3h-6 M11 23h4 M12 26h3" fill="none" stroke="var(--ink)" stroke-width="1.3"/><circle cx="20" cy="30" r="1.6" fill="var(--ink)"/><circle cx="31" cy="30" r="1.6" fill="var(--ink)"/><circle cx="21" cy="14" r="3.5" fill="none" stroke="var(--ink)" stroke-width="1.2"/></svg>
      <p class="value__label">Deliver WOW through service</p>
    </div>
    <span class="values__rule" style="left:537px"></span>
    <div class="value" style="left:524px">
      <svg class="value__icon" viewBox="0 0 46 46"><circle cx="23" cy="23" r="20" fill="none" stroke="var(--ink)" stroke-width="2"/><path d="M23 2 A21 21 0 0 1 23 44" fill="none" stroke="var(--red)" stroke-width="2.5" transform="translate(2 0)"/><path d="M14 33l5-14 9 9z M22 17l2-3 M27 19l4-2 M29 24l3 1" fill="none" stroke="var(--ink)" stroke-width="1.3"/><circle cx="25" cy="12" r="1" fill="var(--red)"/><circle cx="33" cy="14" r="1" fill="var(--red)"/></svg>
      <p class="value__label">Have Fun</p>
    </div>
  </div>

  <div class="contact-bar">
    <svg class="contact__icon" style="left:44px" viewBox="0 0 24 24"><path d="M6 3l4 4-2 3c1 3 3 5 6 6l3-2 4 4-3 3C10 21 3 14 3 6z" fill="var(--red)"/><path d="M15 4a6 6 0 0 1 5 5 M14 7a3 3 0 0 1 3 3" fill="none" stroke="var(--red)" stroke-width="1.6"/></svg>
    <span class="contact contact--phone">800.555.0142</span>
    <span class="contact-bar__divider"></span>
    <svg class="contact__icon" style="left:272px;width:22px;height:22px;top:10px" viewBox="0 0 24 24"><g fill="none" stroke="var(--red)" stroke-width="1.8"><circle cx="12" cy="12" r="10"/><ellipse cx="12" cy="12" rx="4.5" ry="10"/><path d="M2 12h20 M4 6.5h16 M4 17.5h16"/></g></svg>
    <span class="contact contact--web">www.<b>teklogistics</b>.com</span>
  </div>

  <div class="brand">
    <span class="brand__name">TEK</span>
    <span class="brand__sub">LOGISTICS</span>
  </div>
</main>
</body>
</html>
```